Business Card Design for sports performance / psychology company

You can see my website that this is based upon here:
http://www.trelvoxcoaching.co.uk

More than happy to answer any additional questions that you might have

** Happy for any images from Pixelgrove to be used. If I go with your design I will purchase the image for you to use

Target Market(s)

Football players

Industry/Entity Type

Business

Contact Information for Business Card

Name: Dewi Ansell
Title: Clinical Hypnotherapist & Strategist
Email address: dewi@trelvoxcoaching.co.uk
Tel: 07481926657

Font styles to use
Other font styles liked:
• Same font as on website. I'm not actually sure what it is

Requirements
Must have
• Tagline:
• Talent x Focus = Results
• Don't put form down to chance
Nice to have
• Happy for designers to be creative
Should not have

```html
<!DOCTYPE html>
<html lang="en">
<head>
<meta charset="utf-8">
<title>Trelvox Coaching – Business Card</title>
<link rel="stylesheet" href="https://fonts.googleapis.com/css2?family=Jost:wght@400&family=Lato:wght@300;400;700&display=swap">
<style>
  :root {
    --stage: #222222;
    --navy: #221e48;
    --white: #ffffff;
    --ink: #3a3a44;
    --rule: #221e48;
  }
  * { box-sizing: border-box; margin: 0; padding: 0; }
  html, body {
    width: 1189px; height: 1200px; overflow: hidden;
    background: var(--stage);
  }
  .canvas { position: relative; width: 1189px; height: 1200px; }
  .card {
    position: absolute; left: 171px; width: 855px; height: 488px;
    border-radius: 34px;
    box-shadow: 6px 10px 18px rgba(0,0,0,0.55);
  }
  .card--front { top: 67px; background: var(--navy); }
  .card--back { top: 626px; background: var(--white); }

  .front-mark {
    position: absolute; left: 391px; top: 143px;
    width: 74px; height: 74px;
    border: 2px solid var(--white);
  }
  .front-brand {
    position: absolute; left: 0; right: 0; top: 240px;
    text-align: center; color: var(--white);
    font-family: "Jost", sans-serif; font-weight: 400;
    font-size: 70px; letter-spacing: 1px; line-height: 1;
  }
  .front-tagline {
    position: absolute; left: 0; right: 0; top: 320px;
    text-align: center; color: var(--white);
    font-family: "Lato", sans-serif; font-weight: 400; font-size: 23px;
  }

  .back-brand {
    position: absolute; left: 74px; top: 150px; width: 253px;
    text-align: center;
  }
  .back-brand__mark {
    width: 72px; height: 72px; margin: 0 auto 22px;
    background: var(--navy);
  }
  .back-brand__name {
    color: var(--navy);
    font-family: "Jost", sans-serif; font-weight: 400;
    font-size: 34px; line-height: 1.15; letter-spacing: 1px;
  }
  .divider {
    position: absolute; left: 375px; top: 105px;
    width: 1.5px; height: 281px; background: var(--rule);
  }
  .details {
    position: absolute; left: 423px; top: 100px;
    font-family: "Lato", sans-serif; color: var(--ink);
  }
  .person__name { font-size: 33px; color: var(--navy); font-weight: 300; line-height: 1.2; }
  .person__name strong { font-weight: 700; }
  .person__title { font-size: 21.5px; font-weight: 300; margin-top: 2px; }
  .address { margin-top: 54px; font-size: 21.5px; font-weight: 300; line-height: 27px; }
  .contacts { list-style: none; margin-top: 24px; font-size: 22px; font-weight: 300; }
  .contacts li { display: flex; align-items: center; height: 28.5px; }
  .contacts .icon { width: 22px; height: 22px; margin-right: 13px; flex: none; }
  .contacts .domain { color: var(--navy); font-weight: 400; }
</style>
</head>
<body>
<main class="canvas">
  <section class="card card--front">
    <div class="front-mark"></div>
    <h1 class="front-brand">TRELVOX COACHING</h1>
    <p class="front-tagline">Talent x Focus = Results</p>
  </section>

  <section class="card card--back">
    <div class="back-brand">
      <div class="back-brand__mark"></div>
      <p class="back-brand__name">TRELVOX<br>COACHING</p>
    </div>
    <div class="divider"></div>
    <div class="details">
      <p class="person__name"><strong>Dewi</strong> Ansell</p>
      <p class="person__title">Clinical Hypnotherapist &amp; Strategist</p>
      <p class="address">Tamar Innovation Centre<br>Exeter &amp; Welbeck Row, London</p>
      <ul class="contacts">
        <li>
          <svg class="icon" viewBox="0 0 22 22" aria-hidden="true">
            <rect width="22" height="22" rx="3" fill="#221e48"/>
            <path d="M5 9c0-2 2.5-3 6-3s6 1 6 3l-2 1-1-2H8l-1 2z M7 12h8l1 5H6z" fill="#fff"/>
          </svg>07481926657
        </li>
        <li>
          <svg class="icon" viewBox="0 0 22 22" aria-hidden="true">
            <rect width="22" height="22" rx="3" fill="#221e48"/>
            <rect x="4.5" y="6.5" width="13" height="9" fill="none" stroke="#fff" stroke-width="1.3"/>
            <path d="M4.5 6.5l6.5 5 6.5-5M4.5 15.5l5-4.5M17.5 15.5l-5-4.5" fill="none" stroke="#fff" stroke-width="1.1"/>
          </svg>dewi@trelvoxcoaching.co.uk
        </li>
        <li>
          <svg class="icon" viewBox="0 0 22 22" aria-hidden="true">
            <rect width="22" height="22" rx="3" fill="#221e48"/>
            <g fill="none" stroke="#fff" stroke-width="1.1">
              <circle cx="11" cy="11" r="6.5"/>
              <ellipse cx="11" cy="11" rx="3" ry="6.5"/>
              <path d="M4.5 11h13M5.5 7.8h11M5.5 14.2h11"/>
            </g>
          </svg><span>www.<span class="domain">trelvoxcoaching</span>.co.uk</span>
        </li>
      </ul>
    </div>
  </section>
</main>
</body>
</html>
```